Buch-/E-Book-Cover Pathways to Hire & Charm the Locals
Klares Design und rasche Umsetzung aller Änderungswünsche. Vielen Dank, gerne wieder.
Zielgruppe
Ich helfe internationalen Fachkräften Jobs in Deutschland zu finden. Meine Zielgruppe ist hochgebildet (97% mit Uni-Abschluss), spricht fließend englisch, ist global mobil und kommt aus allen Teilen der Welt.
Das PROBLEM MEINER ZIELGRUPPE:
Trotz hervorragender Fähigkeiten scheitert meine Zielgruppe im normalen Bewerbungsprozess. Der Grund: Sie werden nicht als individuelle Person, als Mensch mit Fähigkeiten bewertet - sondern nur als STEREOTYP gesehen. Ich helfe meinen Klienten in ein direktes Gespräch mit den Entscheidern einzutreten - damit sie wieder als einzelner Mensch, als Profi bewertet werden.
Aufgabenstellung
UPDATE: Ich habe ein neues Foto für die Rückseite hochgeladen. Morgen (Donnerstag) sende ich die verschiedenen Entwürfe zum Voting an meine Zielgruppe. Ich hoffe das ich dann innerhalb weniger Tage die Siegerin oder den Sieger bestimmen kann. :)
Aktualisierte Neuauflage meines englischsprachigen Buches 'Pathways to Hire & Charm the Locals'. Buchumschlag design für Verlora BPX Paperback und Hardcover.
Beide Formate sind in den Abmessungen identisch:
Paperback 13,97 x 21,59 cm
Hardcover 13,97 x 21,59 cm
UPDATE: Das Buch hat 159 Seiten.
Die 'Third updated Edition' sollte evtl. in einem Störer hervorgehoben werden.
Das Design muss aus der Masse der Verlora Titel hervorstechen - auch dann wenn man es auf einem Smartphone betrachtet. Das Design soll klar und modern sein. Ich prüfe bei jedem Design ob es zwischen diesen Suchresultaten auffallen würde:
https://www.verlora-shop.de/gp/toplist/books/582913/ref=vx_tl_qrbs_books
Würde ich dieses Buchcover anklicken?
Meine Zielgruppe verdient oberhalb von 60.000€ jährlich. Meine Dienstleistung (Coaching) ist entsprechend teuer. Am Besten denken Designer darüber nach wie über ein *Luxusprodukt* - dass dem Kunden aber gleichzeitig ein höheres Einkommen sichert.
Buchtitel: Pathways to Hire & Charm the Locals
Untertitel: The Newcomers' Manual for Working Abroad Well
Störer oder Teil des Untertitels: Third & Updated Edition
Author: Dana Owerk
Das Verlagslogo füge ich unten in zwei Versionen bei.
WICHTIG: Der Buchumschlag muss allen Verlora BPX Anforderungen entsprechen. (Z.B. Platz für barcode auf der Rückseite etc.) - Designs die diesen Anforderungen nicht entsprechen, scheiden automatisch aus.
Ansonsten habe ich keine Vorgaben.
Weitere Infos:
Klappentext - Rückseite:
German angst rules HR departments and destroys career opportunities for international talent and everyone else who dar..

```html
<!DOCTYPE html>
<html lang="en">
<head>
<meta charset="utf-8">
<title>Pathways to Hire &amp; Charm the Locals – Cover</title>
<link rel="stylesheet" href="https://fonts.googleapis.com/css2?family=Oswald:wght@600&family=Montserrat:wght@500&display=swap">
<style>
  :root {
    --stage: #000000;
    --sky-top: #a2cfe4;
    --sky-mid: #e9f4f9;
    --sky-bottom: #cbe4f0;
    --ink: #16204a;
    --ink-soft: #2a3357;
    --ribbon: #f6a51d;
    --ribbon-ink: #1b1b1b;
    --publisher: #e8642a;
    --illustration-a: #c9a987;
    --illustration-b: #b8dbea;
  }
  * { margin: 0; padding: 0; box-sizing: border-box; }
  html, body {
    width: 1200px; height: 1200px; overflow: hidden;
    background: var(--stage);
  }
  .cover {
    position: absolute; left: 277px; top: 102px;
    width: 680px; height: 996px; overflow: hidden;
    background: linear-gradient(180deg, var(--sky-top) 0%, #c4e2ef 30%, var(--sky-mid) 62%, #dcedf5 82%, var(--sky-bottom) 100%);
  }
  .cover__illustration {
    position: absolute; left: 128px; top: 40px;
    width: 398px; height: 413px; border-radius: 50%;
    background: radial-gradient(circle at 50% 50%, var(--illustration-a) 0%, #d7c2a8 30%, var(--illustration-b) 70%, rgba(184,219,234,0) 100%);
  }
  .cover__ribbon { position: absolute; left: 0; top: 0; }
  .ribbon__label {
    font-family: 'Montserrat', sans-serif; font-weight: 500;
    font-size: 14px; letter-spacing: 1px; fill: var(--ribbon-ink);
  }
  .publisher {
    position: absolute; right: 12px; top: 22px;
    display: flex; align-items: center; gap: 5px;
    font-family: 'Montserrat', sans-serif; font-weight: 500;
    font-size: 13px; color: var(--publisher);
  }
  .publisher__dot { width: 10px; height: 10px; border-radius: 50%; background: var(--publisher); }
  .title {
    position: absolute; left: 0; top: 540px; width: 100%;
    text-align: center; font-family: 'Oswald', sans-serif; font-weight: 600;
    color: var(--ink); text-transform: uppercase; line-height: 1;
  }
  .title__line { display: block; }
  .title__line--small { font-size: 66px; }
  .title__line--mid { font-size: 84px; margin-top: 4px; }
  .title__line--large { font-size: 104px; margin-top: 2px; }
  .subtitle {
    position: absolute; left: 68px; top: 795px; width: 544px; height: 58px;
    border-top: 2px solid var(--ink-soft); border-bottom: 2px solid var(--ink-soft);
    display: flex; align-items: center; justify-content: center;
    font-family: 'Montserrat', sans-serif; font-weight: 500; font-size: 15.5px;
    letter-spacing: 1px; color: var(--ink-soft); text-transform: uppercase;
    white-space: nowrap;
  }
  .author {
    position: absolute; left: 0; top: 910px; width: 100%; text-align: center;
    font-family: 'Montserrat', sans-serif; font-weight: 500; font-size: 28px;
    letter-spacing: 3px; color: var(--ink-soft); text-transform: uppercase;
  }
</style>
</head>
<body>
  <main class="cover">
    <div class="cover__illustration" role="img" aria-label="Illustration of a wooden tree whose branches connect colourful cubes with person icons in a network"></div>

    <svg class="cover__ribbon" width="680" height="260" viewBox="0 0 680 260" aria-hidden="false">
      <polygon points="458,0 522,0 680,158 680,222" fill="var(--ribbon)"/>
      <text class="ribbon__label" x="0" y="0" text-anchor="middle" transform="translate(584,101) rotate(45)">THIRD &amp; UPDATED EDITION</text>
    </svg>

    <div class="publisher"><span class="publisher__dot"></span>Lumora</div>

    <h1 class="title">
      <span class="title__line title__line--small">Pathways to</span>
      <span class="title__line title__line--mid">Hire &amp; Charm</span>
      <span class="title__line title__line--large">the Locals</span>
    </h1>

    <p class="subtitle">The Newcomers' Manual for Working Abroad Well</p>

    <p class="author">Dana Owerk</p>
  </main>
</body>
</html>
```